Design for new eBook - Steady! Bend your habits forward- build wonder, rain, salt and Ember.

GO FOR IT!
The Quiet Orchard Of
Rain, Salt and Ember!

Strong contrasting colors, to make a statement of contrast and power.
This is about duality, turning old relationships into new ones, release old attachments and starting over positively.

Target Market(s)

Relationships; Self Improvement; the quiet orchard of rain, salt and ember.

Requirements
Must have
• Photo; background; strong contrasting colors - as awakening. Make a positive statement about relationships, yet with a bit of mystery and possibly questioning.
• The copy is in the attachment below. This has been edited from what was first put up (professionally advised to do so). Part of the background to show a matrix, if possible, and if used It can very subtle. If using a couple and there is a questioning, there needs to be a coming together...
Nice to have
• I have sent attachments with ideas of what I am looking for. Would like an original type style to use on this book as well as others. Would like to have a style of cover that I could use in the other books. An original type style that would appeal to men and women. Two people can be used, and can be silhouetted. contrasting colors and medium tones, as Turquoise, lavender, etc. makes a good accent color... Include Several different colors on cover.
Should not have
• Cover not to be pastel or use orange (gold is good)
• No tattoos, wedding rings, prissy colors, and not too dark. Nothing referring to a wedding.

```html
<!DOCTYPE html>
<html lang="en">
<head>
<meta charset="utf-8">
<title>Go For It! – eBook Cover</title>
<link rel="stylesheet" href="https://fonts.googleapis.com/css2?family=Caveat+Brush&family=Caveat:wght@600&family=Baloo+2:wght@700&family=Oswald:wght@300&family=Patrick+Hand+SC&display=swap">
<style>
  :root {
    --gold-light: #fbe39a;
    --gold: #e0ad3a;
    --gold-deep: #9a6a14;
    --tagline: #f6c35e;
    --body-text: #ffffff;
    --ink: #140c10;
    --subtitle: #eadfcf;
    --spine: #1b0d28;
  }
  * { margin: 0; padding: 0; box-sizing: border-box; }
  html, body { width: 1200px; height: 900px; overflow: hidden; background: #000; }
  .cover { position: relative; width: 1200px; height: 900px; }

  .gold-text {
    background: linear-gradient(180deg, var(--gold-light) 0%, var(--gold) 45%, var(--gold-deep) 75%, var(--gold) 100%);
    -webkit-background-clip: text;
    background-clip: text;
    color: transparent;
  }

  /* Back cover */
  .back {
    position: absolute; left: 0; top: 0; width: 580px; height: 900px;
    background: linear-gradient(180deg, #1d271b 0%, #4e7a52 14%, #8aa57a 26%, #d7a487 42%, #d27a7c 56%, #ae3a5c 70%, #6e1a3c 84%, #2c0a22 100%);
    text-align: center;
  }
  .back-title {
    margin-top: 24px;
    font-family: "Caveat Brush", cursive;
    font-size: 104px; line-height: 1;
  }
  .back-byline {
    font-family: "Caveat", cursive; font-weight: 600;
    font-size: 46px; line-height: 1; color: var(--ink);
    margin-top: 6px;
  }
  .tagline {
    font-family: "Baloo 2", sans-serif; font-weight: 700; font-style: italic;
    font-size: 24px; line-height: 30px; color: var(--tagline);
    width: 470px; margin: 24px auto 0;
  }
  .blurb {
    font-family: "Oswald", sans-serif; font-weight: 300;
    font-size: 18.5px; line-height: 23.4px; color: var(--body-text);
    text-align: left; padding: 0 40px 0 43px; margin-top: 30px;
  }
  .blurb p { margin-bottom: 10px; }
  .benefits { list-style: none; }
  .benefits li::before { content: "\2022\00a0"; }

  /* Spine */
  .spine {
    position: absolute; left: 580px; top: 0; width: 44px; height: 900px;
    background: linear-gradient(180deg, #2a2430 0%, #24122e 50%, var(--spine) 100%);
  }
  .spine-text {
    position: absolute; left: 50%; top: 650px;
    transform: translate(-50%, 0) rotate(-90deg); transform-origin: center top;
    white-space: nowrap; display: flex; align-items: baseline; gap: 22px;
    width: 0; justify-content: flex-start;
  }
  .spine-inner {
    position: absolute; left: 0; top: -20px;
    display: flex; align-items: baseline; gap: 22px; white-space: nowrap;
  }
  .spine-title { font-family: "Caveat Brush", cursive; font-size: 30px; }
  .spine-author { font-family: "Caveat", cursive; font-weight: 600; font-size: 36px; color: var(--body-text); }

  /* Front cover */
  .front {
    position: absolute; left: 624px; top: 0; width: 576px; height: 900px;
  }
  .front-art {
    position: absolute; inset: 0;
    background:
      radial-gradient(ellipse 220px 140px at 340px 560px, rgba(255,220,150,0.95) 0%, rgba(240,120,90,0.6) 45%, rgba(240,120,90,0) 100%),
      radial-gradient(ellipse 180px 300px at 330px 300px, rgba(120,40,60,0.85) 0%, rgba(120,40,60,0) 100%),
      linear-gradient(180deg, #2f4a4a 0%, #6f9a88 22%, #c8ad86 45%, #d8806e 58%, #5a2146 70%, #24102e 82%, #1a0a24 100%);
  }
  .front-author {
    position: absolute; top: 14px; left: 0; right: 0; text-align: center;
    padding-left: 20px;
    font-family: "Caveat", cursive; font-weight: 600; font-size: 50px; line-height: 1;
  }
  .front-title {
    position: absolute; top: 612px; left: 0; right: 0; text-align: center;
    font-family: "Caveat Brush", cursive; font-size: 140px; line-height: 1;
  }
  .subtitle {
    position: absolute; top: 752px; left: 0; right: 0; text-align: center;
    padding-left: 46px;
    font-family: "Patrick Hand SC", sans-serif; font-size: 38px; line-height: 40px;
    color: var(--subtitle);
  }
</style>
</head>
<body>
<div class="cover">

  <section class="back">
    <h2 class="back-title gold-text">GO FOR IT!</h2>
    <p class="back-byline">By Marisol T. Venn</p>
    <p class="tagline">Through the Ages a select few have passed down a Powerful Secret Knowledge… and All who apply it to their lives gain Power and Success, and know how to create Love, Joy, and Passion in Relationships!</p>
    <div class="blurb">
      <p>By adapting these Secrets… You’ll be Ready to Go For It, and start creating a life that you absolutely love!</p>
      <p style="margin-bottom:0">Learn How To…</p>
      <ul class="benefits">
        <li>Create a Successful, Happy, Loving, &amp; Passionate Relationship – at any age or if you’re straight or gay.</li>
        <li>Let go of relationships that aren’t beneficial.</li>
        <li>Avoid an affair, get over one, or survive one without losses.</li>
        <li>Release old attachments, guilt and fear.</li>
        <li>Create successful strategies for joyfully living in the now, and letting go of pain or suffering from the past.</li>
        <li>Avoid playing games with your self, your partner and with other people, so you can experience authentic, honest, and positive relationships.</li>
        <li>Slow down and appreciate all of the good stuff life has to offer.</li>
        <li>Realize your greatest potentials, and how much you have to share with others.</li>
      </ul>
    </div>
  </section>

  <section class="spine">
    <div class="spine-text">
      <div class="spine-inner">
        <span class="spine-title gold-text">GO FOR IT!</span>
        <span class="spine-author">By Marisol T. Venn</span>
      </div>
    </div>
  </section>

  <section class="front">
    <div class="front-art" role="img" aria-label="Silhouetted couple kissing under a rainbow umbrella at sunset, with a crescent moon and stars in the sky"></div>
    <p class="front-author gold-text">Marisol T. Venn</p>
    <h1 class="front-title gold-text">GO FOR IT!</h1>
    <p class="subtitle">Secret Strategies for Creating<br>a Successful Relationship<br>with Love, Joy &amp; Passion!</p>
  </section>

</div>
</body>
</html>
```